Dermal Care Nursing Circle - Rack Card Design

This is a 2-sided rack card that should be 3.5 inches wide by 8.5 inches tall.

Text (with instructions), logo and website image are attached. For the main image on the front, you can use the attached image, or pull whatever you like off of brightstockpix.example, and we will purchase the photo from the winning design

The front should have text plus a nurse image, the back should have mostly text with the website image and legend.
Updates

We have received many high quality designs, but it is apparent to us that at the print size we are currently using (3.5x8.5), that the image of the homepage on the back is too small, and not legible. As such, we have decided that we would like to go with a horizontal version at 8.5 wide by 5.5 tall, with a larger more legible version of the website on the back and call outs to one side or the other, please resubmit your designs in that format. Thank you, and sorry for the inconvenience. Ray

Industry/Entity Type

Nurse

Font styles to use
Sans Serif

Colors
876aae
6b449b
b7a5cd
e4daeb

Requirements
Must have
• Please use the color palate from the attached logo, and a nursing image on the front.

```html
<!DOCTYPE html>
<html lang="en">
<head>
<meta charset="utf-8">
<title>Dermal Care Nursing Circle – Rack Card</title>
<link href="https://fonts.googleapis.com/css2?family=Questrial&family=Didact+Gothic&display=swap" rel="stylesheet">
<style>
  :root{
    --purple-dark:#6b449b;
    --purple:#876aae;
    --purple-light:#b7a5cd;
    --purple-pale:#e4daeb;
    --charcoal:#3a3a3b;
    --charcoal-deep:#2e2e2f;
    --row-light:#ececec;
    --row-dark:#e0e0e0;
    --text:#4a4a4a;
    --stage:#2a2a2b;
    --white:#ffffff;
  }
  *{box-sizing:border-box;margin:0;padding:0}
  html,body{width:1200px;height:960px;overflow:hidden;background:var(--stage)}
  body{position:relative;font-family:"Didact Gothic",sans-serif;color:var(--text)}

  .card{position:absolute;width:371px;height:900px;background:var(--white);overflow:hidden}
  .card--front{left:228px;top:30px}
  .card--back{left:641px;top:28px}

  /* ---------- front ---------- */
  .front__hallway{position:absolute;left:0;top:0;width:100%;height:209px;
    background:linear-gradient(90deg,#f2e6c8 0%,#e6d3a8 45%,#d9bf8a 100%)}
  .front__cap{position:absolute;left:0;top:0;width:100%;height:176px}
  .brand{position:absolute;display:flex;align-items:center}
  .front .brand{left:0;top:40px;width:100%;justify-content:center;gap:10px}
  .brand__org{font-family:"Questrial",sans-serif;font-size:15px;line-height:1.15;letter-spacing:.06em;text-transform:uppercase;width:110px;text-align:right}
  .brand__rule{width:1px;height:76px}
  .brand__program{font-family:"Questrial",sans-serif;font-size:21px;line-height:1.15;letter-spacing:.02em;text-transform:uppercase}
  .front .brand__org,.front .brand__program{color:var(--purple-dark)}
  .front .brand__rule{background:var(--purple-dark)}

  .front__slogan{position:absolute;left:0;top:209px;width:100%;height:144px;background:var(--charcoal);
    color:var(--white);font-family:"Questrial",sans-serif;text-transform:uppercase;padding:32px 0 0 28px}
  .front__slogan p{line-height:1;white-space:nowrap}
  .front__slogan .l1{font-size:29px;margin-bottom:12px}
  .front__slogan .l2{font-size:22px;margin-bottom:12px}
  .front__slogan .l3{font-size:28px}

  .front__photo{position:absolute;left:0;top:353px;width:100%;height:497px;
    background:linear-gradient(180deg,#efe3c5 0%,#d8cbb6 40%,#8fb7c9 75%,#a8a39a 100%)}
  .url-bar{position:absolute;left:0;width:100%;display:flex;align-items:center;justify-content:center;gap:9px;
    color:var(--white);font-family:"Questrial",sans-serif;font-size:20px}
  .front .url-bar{top:850px;height:50px;background:var(--purple-dark)}
  .url-bar svg{width:14px;height:14px}

  /* ---------- back ---------- */
  .back__cap{position:absolute;left:0;top:0;width:100%;height:140px}
  .back .brand{left:0;top:36px;width:100%;justify-content:center;gap:8px}
  .back .brand__org{font-size:12px;width:90px;color:var(--white)}
  .back .brand__program{font-size:19px;color:var(--white)}
  .back .brand__rule{height:62px;background:var(--white)}

  .back__intro{position:absolute;left:19px;top:160px;width:336px;font-size:13px;line-height:1.25;text-align:left}

  .features{position:absolute;left:0;top:218px;width:100%;list-style:none}
  .feature{position:absolute;left:0;width:100%;height:94px;display:flex;align-items:center;gap:16px;padding:0 22px}
  .feature:nth-child(odd){background:var(--row-light)}
  .feature:nth-child(even){background:var(--row-dark);flex-direction:row-reverse;padding-left:31px}
  .feature:nth-child(1){top:0}
  .feature:nth-child(2){top:100px}
  .feature:nth-child(3){top:200px}
  .feature:nth-child(4){top:300px}
  .feature:nth-child(5){top:401px}
  .feature:nth-child(6){top:502px}
  .feature__icon{flex:none;width:83px;height:83px;border-radius:50%;background:var(--white);border:3px solid var(--purple-dark);
    display:flex;align-items:center;justify-content:center}
  .feature__icon svg{width:46px;height:46px}
  .feature__text{flex:1;font-size:11.5px;line-height:1.3;text-align:left;color:var(--text)}

  .back__more{position:absolute;left:0;top:820px;width:100%;text-align:center;font-family:"Questrial",sans-serif;font-size:23px;color:var(--charcoal)}
  .back .url-bar{top:856px;height:46px;background:var(--charcoal)}
</style>
</head>
<body>

<!-- Front -->
<section class="card card--front front">
  <div class="front__hallway" role="img" aria-label="Warm sunlit hospital corridor with cream walls"></div>
  <svg class="front__cap" viewBox="0 0 371 176" preserveAspectRatio="none" aria-hidden="true">
    <path d="M0 0H371V80Q300 176 185 176Q70 176 0 80Z" fill="#ffffff"/>
  </svg>
  <div class="brand">
    <div class="brand__org">Skyline Skin Foundation</div>
    <div class="brand__rule"></div>
    <div class="brand__program">Dermal Care<br>Nursing<br>Circle</div>
  </div>
  <div class="front__slogan">
    <p class="l1">Inspired by patients</p>
    <p class="l2">Empowered by knowledge</p>
    <p class="l3">Impacting melanoma</p>
  </div>
  <div class="front__photo" role="img" aria-label="Photo of a smiling nurse in blue scrubs pushing a senior patient in a wheelchair along a bright hallway"></div>
  <div class="url-bar">
    <svg viewBox="0 0 16 16" aria-hidden="true"><circle cx="8" cy="8" r="7" fill="none" stroke="#fff" stroke-width="1.4"/><ellipse cx="8" cy="8" rx="3" ry="7" fill="none" stroke="#fff" stroke-width="1.2"/><path d="M1 8H15M2.5 4.5H13.5M2.5 11.5H13.5" stroke="#fff" stroke-width="1.1"/></svg>
    <span>www.DermalCareNurse.example</span>
  </div>
</section>

<!-- Back -->
<section class="card card--back back">
  <svg class="back__cap" viewBox="0 0 371 140" preserveAspectRatio="none" aria-hidden="true">
    <path d="M0 0H371V40Q330 140 185 140Q45 140 0 40Z" fill="#6b449b"/>
  </svg>
  <div class="brand">
    <div class="brand__org">Skyline Skin Foundation</div>
    <div class="brand__rule"></div>
    <div class="brand__program">Dermal Care<br>Nursing<br>Circle</div>
  </div>

  <p class="back__intro">You wear many hats and take care of patients with many different tumor types. Check out DermalCareNurse.example for free access to:</p>

  <ul class="features">
    <li class="feature">
      <div class="feature__icon"><svg viewBox="0 0 48 48" aria-hidden="true"><rect x="4" y="8" width="40" height="32" rx="3" fill="#3a3a3b"/><rect x="8" y="12" width="32" height="7" fill="#fff"/><rect x="8" y="23" width="13" height="13" fill="#fff"/><path d="M25 24H40M25 29H40M25 34H40" stroke="#fff" stroke-width="2.5"/></svg></div>
      <p class="feature__text">Hot off the press! Articles from the Journal of Clinical Care Nursing outlining practical strategies to manage side-effects and promote adherence to melanoma therapies</p>
    </li>
    <li class="feature">
      <div class="feature__icon"><svg viewBox="0 0 48 48" aria-hidden="true"><circle cx="26" cy="10" r="5" fill="#3a3a3b"/><path d="M18 26Q20 17 28 18Q34 19 34 26Z" fill="#3a3a3b"/><circle cx="10" cy="27" r="4" fill="#3a3a3b"/><rect x="15" y="25" width="26" height="6" rx="2" fill="#3a3a3b"/><rect x="5" y="34" width="38" height="4" rx="2" fill="#3a3a3b"/><rect x="5" y="41" width="38" height="3" rx="1.5" fill="#3a3a3b"/></svg></div>
      <p class="feature__text">Visual and text-based therapeutic side effect management tools</p>
    </li>
    <li class="feature">
      <div class="feature__icon"><svg viewBox="0 0 48 48" aria-hidden="true"><path d="M10 16Q10 5 24 5Q38 5 38 16Z" fill="#3a3a3b"/><path d="M22 8H26M24 6V10" stroke="#fff" stroke-width="2"/><circle cx="24" cy="29" r="15" fill="#3a3a3b"/></svg></div>
      <p class="feature__text">A Nurse's Toolkit with extensive melanoma nursing care resources</p>
    </li>
    <li class="feature">
      <div class="feature__icon"><svg viewBox="0 0 48 48" aria-hidden="true"><rect x="8" y="6" width="28" height="36" rx="2" fill="none" stroke="#3a3a3b" stroke-width="3"/><path d="M13 14H30M13 20H30M13 26H24" stroke="#3a3a3b" stroke-width="3"/><path d="M26 36L42 12L45 15L29 38L25 39Z" fill="#3a3a3b"/></svg></div>
      <p class="feature__text">Printable patient resources to provide patients, organized by therapy</p>
    </li>
    <li class="feature">
      <div class="feature__icon"><svg viewBox="0 0 48 48" aria-hidden="true"><circle cx="24" cy="24" r="19" fill="none" stroke="#3a3a3b" stroke-width="2"/><circle cx="24" cy="24" r="14" fill="none" stroke="#3a3a3b" stroke-width="2"/><circle cx="24" cy="24" r="8" fill="none" stroke="#3a3a3b" stroke-width="2"/><circle cx="22" cy="22" r="2.5" fill="#3a3a3b"/><circle cx="28" cy="27" r="1.8" fill="#3a3a3b"/></svg></div>
      <p class="feature__text">An oncology nurse community forum to share successes, challenges, insights, and solutions</p>
    </li>
    <li class="feature">
      <div class="feature__icon"><svg viewBox="0 0 48 48" aria-hidden="true"><path d="M4 12Q14 8 23 13V40Q14 35 4 38Z" fill="#3a3a3b"/><path d="M44 12Q34 8 25 13V40Q34 35 44 38Z" fill="#3a3a3b"/><path d="M8 17Q14 15 20 18V35Q14 32 8 33Z" fill="#fff"/><path d="M40 17Q34 15 28 18V35Q34 32 40 33Z" fill="#fff"/></svg></div>
      <p class="feature__text">Online educational modules, newsfeeds, and other material to keep you up to date</p>
    </li>
  </ul>

  <p class="back__more">And much more!</p>
  <div class="url-bar">
    <svg viewBox="0 0 16 16" aria-hidden="true"><circle cx="8" cy="8" r="7" fill="none" stroke="#fff" stroke-width="1.4"/><ellipse cx="8" cy="8" rx="3" ry="7" fill="none" stroke="#fff" stroke-width="1.2"/><path d="M1 8H15M2.5 4.5H13.5M2.5 11.5H13.5" stroke="#fff" stroke-width="1.1"/></svg>
    <span>www.DermalCareNurse.example</span>
  </div>
</section>

</body>
</html>
```